Want a package created for a new protein bar

We would like a new package created for a new protein bar project The name of the bar will be VORNBar a real food protein bar, we would like a ‘window’ on the package of bar like Brisk Mell bar below in images.

VORNBar
‘Super Food Bar’
14g of Whey Protein
The package film size is the following 12cm width x 15cm Length,
Flavor Peanut Chocolate Chip, additional information will be attached shortly like nutrition facts,

Target Market(s)

fitness market, bodybuilders, athletes, everyday people

Industry/Entity Type

Health Product

Logo Text

VORNBar

Font styles to use
Serif
Sans Serif
Decorative

Requirements
Must have
• Package window

```html
<!DOCTYPE html>
<html lang="en">
<head>
<meta charset="utf-8">
<title>VORNBar – Peanut Chocolate Chip Wrapper</title>
<link href="https://fonts.googleapis.com/css2?family=Barlow:wght@400;700&family=Oswald:wght@600;700&display=swap" rel="stylesheet">
<style>
  :root {
    --paper: #ffffff;
    --wrapper-black: #0e0e0e;
    --slate: #263840;
    --ink-white: #ffffff;
    --flavour-orange: #f06a13;
    --strength-blue: #436a8c;
    --peanut-red: #d9340e;
    --peanut-light: #f08a3a;
    --cocoa: #5a0400;
    --cocoa-light: #8a2a20;
  }
  html, body {
    margin: 0;
    padding: 0;
    overflow: hidden;
    background: var(--paper);
  }
  .canvas {
    position: relative;
    width: 1200px;
    height: 829px;
    background: var(--paper);
    overflow: hidden;
  }

  /* Front face */
  .front-face {
    position: absolute;
    left: 55px;
    top: 163px;
    width: 689px;
    height: 402px;
    background: var(--wrapper-black);
  }
  .brand-panel {
    position: absolute;
    left: 110px;
    top: 0;
    width: 469px;
    height: 179px;
    background: var(--slate);
    border-radius: 0 0 24px 24px;
    color: var(--ink-white);
    text-align: center;
  }
  .brand-name {
    margin: 0;
    padding-top: 4px;
    font-family: "Barlow", sans-serif;
    font-weight: 700;
    font-size: 100px;
    line-height: 1;
    letter-spacing: 0;
  }
  .brand-tagline {
    margin: 6px 0 0;
    font-family: "Barlow", sans-serif;
    font-weight: 400;
    font-size: 47px;
    line-height: 1;
    letter-spacing: 9px;
    text-indent: 9px;
  }
  .feature-icons {
    position: absolute;
    left: 0;
    top: 0;
    width: 689px;
    height: 402px;
  }
  .flavour-tab {
    position: absolute;
    left: 55px;
    bottom: 0;
    width: 602px;
    height: 59px;
    background: var(--flavour-orange);
    border-radius: 27px 27px 0 0;
    color: var(--ink-white);
    font-family: "Oswald", sans-serif;
    font-weight: 700;
    font-size: 44px;
    line-height: 59px;
    letter-spacing: 6px;
    text-indent: 6px;
    text-align: center;
    white-space: nowrap;
  }

  /* Clear window between front face and side gusset */
  .package-window {
    position: absolute;
    left: 744px;
    top: 163px;
    width: 236px;
    height: 402px;
    background: transparent;
  }

  /* Side gusset */
  .side-strip {
    position: absolute;
    left: 980px;
    top: 163px;
    width: 137px;
    height: 402px;
    background: var(--wrapper-black);
  }
  .side-strip-text {
    position: absolute;
    left: 0;
    top: 0;
    width: 402px;
    height: 137px;
    transform-origin: top left;
    transform: translate(137px, 0) rotate(90deg);
    font-family: "Oswald", sans-serif;
    font-weight: 700;
    color: var(--ink-white);
  }
  .side-strip-text span {
    position: absolute;
    line-height: 1;
    white-space: nowrap;
  }
  .protein-amount {
    left: 6px;
    top: 18px;
    font-size: 86px;
    letter-spacing: -4px;
    color: var(--flavour-orange);
  }
  .protein-unit {
    left: 68px;
    top: 78px;
    font-size: 30px;
    color: var(--flavour-orange);
  }
  .claim {
    font-size: 35px;
  }
  .claim-whey { left: 96px; top: 26px; letter-spacing: 3px; }
  .claim-protein { left: 98px; top: 69px; letter-spacing: 1.5px; }
  .claim-super { left: 275px; top: 26px; letter-spacing: 2px; }
  .claim-food { left: 275px; top: 69px; letter-spacing: 2px; }
  .claim-divider {
    position: absolute;
    left: 251px;
    top: 25px;
    width: 3px;
    height: 77px;
    background: repeating-linear-gradient(to bottom, var(--flavour-orange) 0 4px, transparent 4px 7px);
  }
</style>
</head>
<body>
<div class="canvas">
  <section class="front-face">
    <header class="brand-panel">
      <h1 class="brand-name">VORNBar</h1>
      <p class="brand-tagline">A Real Food Bar</p>
    </header>

    <svg class="feature-icons" viewBox="0 0 689 402" aria-label="Feature icons">
      <defs>
        <radialGradient id="peanut-tone" cx="50%" cy="50%" r="50%">
          <stop offset="0%" stop-color="var(--peanut-light)"/>
          <stop offset="100%" stop-color="var(--peanut-red)"/>
        </radialGradient>
        <radialGradient id="chip-tone" cx="50%" cy="50%" r="50%">
          <stop offset="0%" stop-color="var(--cocoa-light)"/>
          <stop offset="100%" stop-color="var(--cocoa)"/>
        </radialGradient>
      </defs>
      <g class="icon-strength">
        <circle cx="187" cy="262" r="52" fill="var(--strength-blue)"/>
        <g fill="var(--ink-white)">
          <rect x="145" y="257" width="4" height="12" rx="1"/>
          <rect x="151" y="246" width="9" height="34" rx="3"/>
          <rect x="162" y="240" width="8" height="46" rx="3"/>
          <rect x="170" y="259" width="34" height="8" rx="1"/>
          <rect x="204" y="240" width="8" height="46" rx="3"/>
          <rect x="214" y="246" width="9" height="34" rx="3"/>
          <rect x="225" y="257" width="4" height="12" rx="1"/>
        </g>
      </g>
      <circle cx="351" cy="262" r="52" fill="url(#peanut-tone)" role="img" aria-label="Peanut icon"/>
      <circle cx="506" cy="262" r="52" fill="url(#chip-tone)" role="img" aria-label="Chocolate chip icon"/>
    </svg>

    <div class="flavour-tab">PEANUT CHOCOLATE CHIP</div>
  </section>

  <div class="package-window" role="img" aria-label="Clear film window showing the bar inside"></div>

  <aside class="side-strip">
    <div class="side-strip-text">
      <span class="protein-amount">14</span>
      <span class="protein-unit">g</span>
      <span class="claim claim-whey">WHEY</span>
      <span class="claim claim-protein">PROTEIN</span>
      <div class="claim-divider"></div>
      <span class="claim claim-super">SUPER</span>
      <span class="claim claim-food">FOOD</span>
    </div>
  </aside>
</div>
</body>
</html>
```